Travel agency website refresh

I want to refresh and simplify my current Wordpress.com website. Same general color scheme but modernize and make it user friendly for all devices. Must work with Wordpress. No live booking engines. We are a boutique luxury travel agency. Think luxury, vacation, boho chic, elegant, lush, tropical, cruises, first class. Romance and adventure.
Updates

I’ve guaranteed the project so I’m hoping to see more quality entries to make a decision

Target Market(s)

Luxury travelers

Industry/Entity Type

Travel

Coding

Coded - Design and coding required

Number of Pages Required

5+ page

Font styles to use
Sans Serif

Colors
0094D4
00A9DD
6FCCEA
C7EBF8
E9F6FB

Requirements
Must have
• Compatible with Wordpress.com, homepage, about page, contact page, faq page
Nice to have
• The homepage should quickly tell the consumer the type of travel I specialize in. My current website has this (journeywithmerel.example). I’d like to incorporate the about me as a preview on the home page.
Should not have
• Harsh colors, look generic

```html
<!DOCTYPE html>
<html lang="en">
<head>
<meta charset="utf-8">
<title>Journeys by Merel — Landing Page Mobile View</title>
<link href="https://fonts.googleapis.com/css2?family=Playfair+Display:wght@400;700&family=Lato:wght@400;700&display=swap" rel="stylesheet">
<style>
  :root{
    --blue-deep:#0094D4;
    --blue:#00A9DD;
    --blue-soft:#6FCCEA;
    --blue-pale:#C7EBF8;
    --blue-mist:#E9F6FB;
    --sand:#C9B49E;
    --sand-dark:#B59E86;
    --frame:#5d5d5d;
    --ink:#444;
    --muted:#777;
    --white:#fff;
    --serif:'Playfair Display', serif;
    --sans:'Lato', sans-serif;
  }
  *{box-sizing:border-box;margin:0;padding:0}
  html,body{width:1200px;height:771px;overflow:hidden}
  body{position:relative;background:var(--sand);font-family:var(--sans);color:var(--ink)}

  /* Left info panel */
  .intro{position:absolute;left:0;top:0;width:249px;height:771px;background:var(--white)}
  .intro-title{position:absolute;left:56px;top:150px;font-family:var(--serif);font-weight:700;font-size:28px;line-height:36px;color:var(--blue)}
  .intro-sub{position:absolute;left:56px;top:258px;font-size:19px;line-height:25px;color:var(--muted)}
  .intro-band{position:absolute;left:0;top:446px;width:249px;height:325px;background:var(--blue);border-top-right-radius:26px}
  .intro-icon{position:absolute;left:86px;top:405px;width:78px;height:70px;background:#6a6a6a;display:flex;align-items:center;justify-content:center}
  .intro-icon span{width:24px;height:24px;border-radius:50%;background:var(--white)}

  /* Phone screens */
  .screen{position:absolute;background:var(--white);overflow:hidden}
  .phone-footer{left:286px;top:-20px;width:256px;height:338px;border:5px solid var(--frame);border-top:none;border-radius:0 0 28px 28px}
  .phone-home{left:286px;top:339px;width:256px;height:450px;border:5px solid var(--frame);border-bottom:none;border-radius:30px 30px 0 0}
  .page-why{left:600px;top:0;width:254px;height:771px;border-left:5px solid var(--frame);border-right:5px solid var(--frame)}
  .page-services{left:903px;top:0;width:265px;height:771px;border-left:4px solid #d9d9d9;border-right:4px solid #d9d9d9}

  /* Footer screen */
  .foot-body{padding:26px 22px 0}
  .foot-heading{font-family:var(--serif);color:var(--blue);font-size:10.5px;line-height:14px;margin-bottom:4px}
  .foot-list{list-style:none;font-size:8px;line-height:11.6px;color:#555;margin-bottom:12px}
  .foot-bar{position:absolute;left:0;right:0;bottom:0;height:36px;background:var(--sand-dark);color:var(--white);font-size:7px;text-align:center;line-height:28px;font-family:var(--serif)}

  /* Home screen */
  .site-head{height:44px;display:flex;align-items:center;justify-content:space-between;padding:0 16px}
  .brand{display:flex;align-items:center;gap:6px;font-family:var(--serif);font-size:8px;font-weight:700;color:var(--blue-deep);line-height:9px}
  .brand-dot{width:20px;height:20px;border-radius:50%;background:var(--blue-soft)}
  .menu-btn{width:20px;height:20px;border:1px solid var(--sand-dark);display:flex;flex-direction:column;justify-content:center;gap:3px;padding:0 4px}
  .menu-btn span{height:1px;background:var(--sand-dark)}
  .hero{position:absolute;left:0;top:44px;width:100%;height:420px;background:linear-gradient(180deg,#cfe6f1 0%,#e8eef0 35%,#d8c6b2 70%,#b89f86 100%)}
  .hero-title{position:absolute;left:10px;right:10px;top:40px;font-family:var(--serif);font-weight:400;font-size:17px;line-height:24px;text-align:center;color:#555}
  .hero-text{position:absolute;left:20px;right:20px;top:94px;font-size:7.5px;line-height:11.5px;letter-spacing:.3px;text-align:center;color:var(--white);text-transform:uppercase}
  .hero-btn{position:absolute;left:22px;right:22px;top:182px;height:14px;background:var(--sand-dark);color:var(--white);font-size:6.5px;letter-spacing:1px;text-align:center;line-height:14px}
  .hero-links{position:absolute;left:27px;top:226px;list-style:none;font-size:7px;letter-spacing:.8px;color:var(--white);line-height:25px}

  /* Why book screen */
  .photo{position:absolute}
  .why-divider{position:absolute;left:0;right:0;top:438px;height:4px;background:#8c8c8c}
  .insight{position:absolute;left:14px;right:14px;top:474px;height:76px;background:var(--blue-soft);border-radius:5px;padding:10px 12px;color:var(--white)}
  .insight h3{font-weight:400;font-size:11px;margin-bottom:8px}
  .insight p{font-size:6.5px;line-height:8.5px;padding-left:10px}
  .reasons{position:absolute;left:14px;top:554px;list-style:none;font-size:11px;color:#555}
  .reasons li{height:40.5px;display:flex;align-items:center;gap:10px}
  .reasons li::before{content:"";border-left:6px solid #555;border-top:4px solid transparent;border-bottom:4px solid transparent}
  .why-title{position:absolute;left:0;right:0;top:736px;text-align:center;font-family:var(--serif);font-weight:400;font-size:16px;color:#555}

  /* Services screen */
  .svc-title{position:absolute;left:14px;top:54px;font-family:var(--serif);font-weight:400;font-size:17px;color:var(--muted)}
  .svc-title span{color:var(--blue-soft)}
  .svc-intro{position:absolute;left:14px;right:14px;top:78px;font-size:8.5px;line-height:11px;color:#666}
  .beach{position:absolute;left:0;right:0;top:127px;height:226px;background:linear-gradient(180deg,#7fd0ee 0%,#bfe6f3 45%,#6fcfe0 75%,#8fd6e6 100%)}
  .beach-card{position:absolute;left:8px;width:210px;top:138px;height:88px;background:rgba(255,255,255,.35);padding:8px;color:var(--white)}
  .beach-card h3{font-family:var(--serif);font-weight:400;font-size:9px;margin-bottom:4px}
  .beach-card p{font-size:7px;line-height:9.5px}
  .tile{position:absolute;width:115px;display:flex;align-items:flex-end;justify-content:center;padding-bottom:6px;font-family:var(--serif);font-size:7.5px;color:var(--white);letter-spacing:.4px}
  .faq{position:absolute;left:0;right:0;top:628px;height:143px;background:var(--blue-mist);padding:26px 14px}
  .faq h2{font-family:var(--serif);font-weight:400;font-size:17px;line-height:18px;color:var(--muted)}
  .faq h2 span{display:block;color:var(--blue-deep)}
  .faq p{font-size:8.5px;line-height:11px;color:#666;margin-top:12px}
</style>
</head>
<body>

<aside class="intro">
  <h1 class="intro-title">Journeys by<br>Merel</h1>
  <p class="intro-sub">Landing Page<br>Mobile View</p>
  <div class="intro-band"></div>
  <div class="intro-icon"><span></span></div>
</aside>

<section class="screen phone-footer">
  <div class="foot-body">
    <h4 class="foot-heading">Services</h4>
    <ul class="foot-list">
      <li>Custom Travel</li><li>Family Vacations</li><li>Honeymoon and Romance</li>
      <li>River Cruises</li><li>Villa Rentals</li><li>Group Travel</li><li>Cruising</li>
    </ul>
    <h4 class="foot-heading">Forms &amp; Questionnaires</h4>
    <ul class="foot-list">
      <li>Booking Form</li><li>Babymoon Questionnaire</li><li>Destination Wedding Questionnaire</li>
      <li>Family Travel Questionnaire</li><li>Honeymoon Questionnaire</li><li>Honeymoon Gift Deposit</li>
      <li>Plan To Go Service Agreement</li>
    </ul>
  </div>
  <div class="foot-bar">© 2024 Journeys by Merel. All Rights Reserved.</div>
</section>

<section class="screen phone-home">
  <header class="site-head">
    <div class="brand"><span class="brand-dot"></span>JOURNEYS<br>BY MEREL</div>
    <div class="menu-btn"><span></span><span></span><span></span></div>
  </header>
  <div class="hero" role="img" aria-label="Photo of smiling travellers on a sunny terrace">
    <h2 class="hero-title">Experience the Luxury of Personalized Travel</h2>
    <p class="hero-text">I've come nose-to-nose with a giraffe during an African safari, I've strolled along the ancient pathways of Machu Picchu and walked along the Great Wall of China. I've explored the Australian outback, and I've gone on many more adventures.</p>
    <div class="hero-btn">EXPLORE</div>
    <ul class="hero-links">
      <li>CUSTOM TRAVEL ›</li><li>FAMILY VACATIONS ›</li><li>HONEYMOON AND ROMANCE ›</li>
    </ul>
  </div>
</section>

<section class="screen page-why">
  <div class="photo" role="img" aria-label="Photo of a couple reading a map outdoors" style="left:0;right:0;top:0;height:162px;background:linear-gradient(135deg,#3d3a33,#8a7358 55%,#c9b08a)"></div>
  <div class="photo" role="img" aria-label="Photo of a family walking on a white beach" style="left:0;width:122px;top:168px;height:118px;background:linear-gradient(180deg,#7fc6e4,#e9f2f3 55%,#efe4cf)"></div>
  <div class="photo" role="img" aria-label="Photo of a family wading on a sunny shore" style="left:126px;right:0;top:168px;height:118px;background:linear-gradient(180deg,#9fd7ee,#f2efe6 60%,#e6d4b7)"></div>
  <div class="photo" role="img" aria-label="Photo of travellers resting on a hillside" style="left:0;width:122px;top:292px;height:118px;background:linear-gradient(180deg,#c6cdd0,#b49a76)"></div>
  <div class="photo" role="img" aria-label="Photo of a spa massage" style="left:126px;right:0;top:292px;height:118px;background:linear-gradient(135deg,#6b3e2a,#c48b66 60%,#e8c9a9)"></div>
  <div class="why-divider"></div>
  <div class="insight">
    <h3>▾&nbsp; For Expert Insights</h3>
    <p>From hidden gems to insider tips, my expertise helps you plan a trip that feels effortless.</p>
  </div>
  <ul class="reasons">
    <li>To Save You Time</li>
    <li>To Save You Money</li>
    <li>To Personalize Your Vacation</li>
    <li>To Be There When You need Us</li>
  </ul>
  <h2 class="why-title">Why Book With Us</h2>
</section>

<section class="screen page-services">
  <h2 class="svc-title">Tailored <span>Travel Services</span></h2>
  <p class="svc-intro">At Journeys by Merel, we specialize in creating personalized travel experiences that cater to your unique preferences and desires.</p>
  <div class="beach" role="img" aria-label="Photo of an infinity pool overlooking a tropical sea with palms">
    <div class="beach-card">
      <h3>Tailored Travel Services</h3>
      <p>At Journeys by Merel, we specialize in crafting personalized experiences that cater to your tastes and desires.</p>
    </div>
  </div>
  <div class="tile" role="img" aria-label="Photo of a river cruise ship below a hillside town" style="left:14px;top:365px;height:120px;background:linear-gradient(180deg,#8fb7c9,#5f7f5a 60%,#3f5f6e)">RIVER CRUISES</div>
  <div class="tile" role="img" aria-label="Photo of a luxury villa by a pool" style="left:134px;top:365px;height:120px;background:linear-gradient(180deg,#6d8a6a,#9a8b73 55%,#6fbcd0)">VILLA RENTALS</div>
  <div class="tile" role="img" aria-label="Photo of a smiling group of travellers" style="left:14px;top:490px;height:120px;background:linear-gradient(180deg,#7fb4d8,#c9a48a 55%,#6d89b8)">GROUP TRAVEL</div>
  <div class="tile" role="img" aria-label="Photo of a cruise ship deck with pool" style="left:134px;top:490px;height:120px;background:linear-gradient(180deg,#9cc9e4,#e7eef2 50%,#4db4dc)">CRUISES</div>
  <div class="faq">
    <h2>Got Questions?<span>We've Got Answers!</span></h2>
    <p>Explore our frequently asked questions to find out everything you need to know about planning your next adventure with Journeys by Merel.</p>
  </div>
</section>

</body>
</html>
```